Tessbury Pure Twist Label

We are looking for a label for our blueberry vodka and lemonade ready-to-drink cocktail. we would like the ingredients (vodka, lemon juice, cane sugar, blueberries) discretely displayed on the label. We would also like 15% alc/vol (30 proof) on the label. The label is for a 12-ounce slim can. We would also like the Surgeon Generals warning ion the label

Target Market(s)

Spike seltzer and ready to drink cocktail drinkers

Font styles to use
Decorative

Requirements
Must have
• Surgeon General warning, 15% alc/vol (30 proof) 12 ounces., Ingredients

```html
<!DOCTYPE html>
<html lang="en">
<head>
<meta charset="utf-8">
<title>Tessbury Pure Twist – Blueberry Vodka &amp; Lemonade Label</title>
<link rel="stylesheet" href="https://fonts.googleapis.com/css2?family=Rye&family=Alfa+Slab+One&family=Lobster&family=Libre+Baskerville:wght@700&family=Arimo:wght@400;700&display=swap">
<style>
  :root {
    --backdrop: #dde4e2;
    --navy: #1d2270;
    --royal: #2d2f94;
    --sky-deep: #6f97d4;
    --sky-light: #cfdcef;
    --lemon: #f2c11c;
    --white: #ffffff;
    --band-white: #eef0f4;
    --berry: #3d4f96;
    --berry-soft: #5a6fb4;
  }
  * { box-sizing: border-box; margin: 0; padding: 0; }
  html, body { width: 1200px; height: 800px; overflow: hidden; }
  body { background: var(--backdrop); position: relative; font-family: "Arimo", Arial, sans-serif; }

  .label { position: absolute; left: 150px; top: 60px; width: 900px; height: 660px; overflow: hidden; background: var(--navy); box-shadow: 0 10px 30px rgba(0,0,0,.12); }

  .sky-art { position: absolute; left: 180px; top: 0; width: 720px; height: 450px;
    background: linear-gradient(180deg, var(--sky-deep) 0%, #9fbbe4 45%, var(--sky-light) 100%); }
  .lower-field { position: absolute; left: 0; top: 450px; width: 900px; height: 140px; background: var(--navy); }
  .band-white { position: absolute; left: 0; top: 590px; width: 900px; height: 30px; background: var(--band-white); }
  .band-navy { position: absolute; left: 0; top: 620px; width: 900px; height: 40px; background: var(--navy); }

  .back-panel { position: absolute; left: 0; top: 0; width: 180px; height: 590px; background: var(--royal); color: var(--white); }
  .ingredients { position: absolute; left: 14px; top: 18px; width: 160px; font-size: 12px; line-height: 1.35; white-space: nowrap; }
  .ingredients-title { text-transform: uppercase; }
  .panel-rule { position: absolute; left: 10px; top: 92px; width: 160px; height: 1px; background: var(--white); }
  .warning { position: absolute; right: 14px; top: 108px; height: 350px; width: 150px; writing-mode: vertical-rl; font-size: 12.5px; line-height: 1.3; text-align: justify; }
  .warning strong { font-weight: 700; }
  .code-box { position: absolute; left: 10px; top: 470px; width: 72px; height: 112px; background: var(--white); }

  .berry-art { position: absolute; left: 566px; top: 372px; width: 58px; height: 58px; border-radius: 50%;
    background: radial-gradient(circle at 40% 35%, var(--berry-soft) 0%, var(--berry) 70%); }

  .front-panel { position: absolute; left: 560px; top: 0; width: 330px; height: 660px; text-align: center; }
  .tagline { position: absolute; top: 24px; width: 100%; font-family: "Rye", serif; font-size: 16px; color: #eef3fb; letter-spacing: .5px; }
  .brand { position: absolute; top: 82px; left: 0; width: 100%; display: flex; justify-content: center; align-items: center; gap: 12px; }
  .brand-dot { width: 46px; height: 46px; border-radius: 50%; background: var(--lemon); flex: none; }
  .brand-name { font-family: "Libre Baskerville", serif; font-weight: 700; font-size: 19px; line-height: 1.2; color: var(--navy); text-align: left; }
  .title { position: absolute; left: 0; width: 100%; color: var(--navy); -webkit-text-stroke: 6px var(--white); paint-order: stroke fill; }
  .title-blueberry { top: 198px; font-family: "Rye", serif; font-size: 46px; }
  .title-vodka { top: 262px; font-family: "Alfa Slab One", serif; font-size: 50px; letter-spacing: 1px; }
  .title-amp { top: 332px; font-family: "Alfa Slab One", serif; font-size: 38px; }
  .title-lemonade { top: 372px; left: 20px; font-family: "Lobster", cursive; font-size: 50px; color: var(--lemon); -webkit-text-stroke: 6px var(--white); transform: rotate(-6deg); }
  .abv { position: absolute; top: 518px; width: 100%; font-size: 15px; font-weight: 700; color: var(--white); }
  .volume { position: absolute; top: 591px; width: 100%; font-size: 23px; font-weight: 700; color: #111; }
  .volume small { font-size: 17px; }
</style>
</head>
<body>
  <main class="label">
    <div class="sky-art" role="img" aria-label="Painted blue sky with soft white clouds"></div>
    <div class="lower-field"></div>
    <div class="band-white"></div>
    <div class="band-navy"></div>

    <section class="back-panel">
      <p class="ingredients"><span class="ingredients-title">Ingredients:</span><br>Vodka, Lemon Juice,<br>Cane Sugar, Blueberries</p>
      <div class="panel-rule"></div>
      <p class="warning"><strong>GOVERNMENT WARNING:</strong> (1) According to the Surgeon General, women should not drink alcoholic beverages during pregnancy because of the risk of birth defects. (2) Consumption of alcoholic beverages impairs your ability to drive a car or operate machinery, and may cause health problems.</p>
      <div class="code-box"></div>
    </section>

    <div class="berry-art" role="img" aria-label="Cluster of blueberries with green leaves"></div>

    <section class="front-panel">
      <p class="tagline">Ready to Drink Cocktail</p>
      <div class="brand">
        <span class="brand-dot"></span>
        <span class="brand-name">Tessbury<br>Pure Twist</span>
      </div>
      <h1 class="title title-blueberry">BLUEBERRY</h1>
      <p class="title title-vodka">VODKA</p>
      <p class="title title-amp">&amp;</p>
      <p class="title title-lemonade">Lemonade</p>
      <p class="abv">15% alc/vol (30 proof)</p>
      <p class="volume">12 <small>fl.oz</small></p>
    </section>
  </main>
</body>
</html>
```